Coin Donation Box Home version ELEGANT

The idea is to hand out/mail a coin donation box that can be folded/assembled by the receiving party. It should be attractive so people would put it on their desk/night stand to collect change, with instructions on the bottom how to then bring it in for donation to charitable organizations. Similar to Veltara Halloween idea where boxes are shipped to schools, assembled by kids, then carried around for donations. This one should be different - it stays at the person's house until its filled, so should be more durable/attractive. Maybe reusable too? What material - cardboard, plastic, any other new cool materials? Will need logos/instructions. Classy and elegant to encourage prominent display - like a design piece rather than bright in-store ones. maybe the top cover, when opened, has the information and instructions. maybe the size of the rectangular Softora box?
Updates

Target Market(s)

families, offices

Industry/Entity Type

Charity

Font styles to use
Serif

Colors

Designer to choose colors to be used in the design.

Requirements
Must have
• Easy to self-assemble, inexpensive to mass produce, durable to hold heavy coins.
Nice to have
• Elegant - something a person would like to display on their desk or night stand. People use jars at home to dump change our of their pockets in the evening. This can be an alternative, and used for charity donations.

```html
<!DOCTYPE html>
<html lang="en">
<head>
<meta charset="utf-8">
<title>Coin Donation Box – Outside Dieline</title>
<link rel="stylesheet" href="https://fonts.googleapis.com/css2?family=Poppins:wght@400;500;600&family=Great+Vibes&family=Source+Sans+3:wght@400&display=swap">
<style>
  :root {
    --paper: #ffffff;
    --ink: #111111;
    --navy: #012050;
    --navy-wave: #0b3466;
    --glow: #0a5a93;
    --gold-light: #f1d796;
    --gold-mid: #d9b26a;
    --gold-deep: #b98a45;
    --band-rule: #3a79a0;
    --cut: #e0262a;
    --fold: #1f8fd6;
    --logo-text: #ffffff;
    --bloom-1: #a13a55;
    --bloom-2: #5b2a5e;
    --bloom-3: #e9e2cf;
  }
  html, body {
    margin: 0;
    padding: 0;
    width: 923px;
    height: 1200px;
    overflow: hidden;
    background: var(--paper);
  }
  .sheet {
    position: relative;
    width: 923px;
    height: 1200px;
  }
  .dieline {
    position: absolute;
    inset: 0;
    width: 923px;
    height: 1200px;
  }
  .concept-kicker {
    font-family: "Poppins", sans-serif;
    font-weight: 400;
    font-size: 30px;
    fill: var(--ink);
  }
  .concept-title {
    font-family: "Poppins", sans-serif;
    font-weight: 500;
    font-size: 58px;
    fill: var(--ink);
  }
  .legend-label {
    font-family: "Source Sans 3", sans-serif;
    font-size: 27px;
    fill: var(--ink);
  }
  .tagline {
    font-family: "Great Vibes", cursive;
    font-size: 34px;
  }
  .tagline--gold { fill: var(--gold-mid); }
  .tagline--navy { fill: var(--navy); }
  .brand-name {
    font-family: "Poppins", sans-serif;
    font-weight: 500;
    font-size: 18px;
    fill: var(--logo-text);
  }
  .brand-note {
    font-family: "Poppins", sans-serif;
    font-weight: 400;
    font-size: 8px;
    fill: var(--logo-text);
  }
  .cut-line { fill: none; stroke: var(--cut); stroke-width: 1.5; }
  .fold-line { fill: none; stroke: var(--fold); stroke-width: 1.3; stroke-dasharray: 9 6; }
  .wave-band { fill: var(--navy-wave); }
  .band-rule { stroke: var(--band-rule); stroke-width: 2; }
</style>
</head>
<body>
<main class="sheet">
  <svg class="dieline" viewBox="0 0 1536 2000" xmlns="http://www.w3.org/2000/svg">
    <defs>
      <linearGradient id="gold-band" x1="0" x2="1" y1="0" y2="0">
        <stop offset="0" stop-color="var(--gold-light)"/>
        <stop offset="0.3" stop-color="var(--gold-mid)"/>
        <stop offset="0.55" stop-color="var(--gold-deep)"/>
        <stop offset="0.8" stop-color="var(--gold-light)"/>
        <stop offset="1" stop-color="var(--gold-mid)"/>
      </linearGradient>
      <linearGradient id="gold-bar" x1="0" x2="0" y1="0" y2="1">
        <stop offset="0" stop-color="var(--gold-light)"/>
        <stop offset="1" stop-color="var(--gold-deep)"/>
      </linearGradient>
      <radialGradient id="panel-glow">
        <stop offset="0" stop-color="var(--glow)" stop-opacity="0.9"/>
        <stop offset="1" stop-color="var(--navy)" stop-opacity="0"/>
      </radialGradient>
      <radialGradient id="bouquet-tone">
        <stop offset="0" stop-color="var(--bloom-3)"/>
        <stop offset="0.5" stop-color="var(--bloom-1)"/>
        <stop offset="1" stop-color="var(--bloom-2)" stop-opacity="0.85"/>
      </radialGradient>
      <clipPath id="box-shape">
        <path id="box-outline" d="M652 160 V140 A45 45 0 0 1 697 95 H841 A45 45 0 0 1 886 140 V160 L1105 340 L1472 980 L1100 1632 H932 V1660 Q932 1690 905 1705 Q932 1730 932 1760 V1885 H607 V1760 Q607 1730 634 1705 Q607 1690 607 1660 V1632 H440 L64 980 L432 340 Z"/>
      </clipPath>
    </defs>

    <!-- presentation heading -->
    <text class="concept-kicker" x="275" y="158" text-anchor="middle">Design Concept for</text>
    <text class="concept-title" x="274" y="227" text-anchor="middle">OUTSIDE</text>

    <!-- printed box artwork -->
    <g class="box-artwork" clip-path="url(#box-shape)">
      <rect x="0" y="0" width="1536" height="2000" fill="var(--navy)"/>

      <circle cx="705" cy="560" r="200" fill="url(#panel-glow)"/>
      <circle cx="820" cy="1420" r="200" fill="url(#panel-glow)"/>

      <rect class="wave-band" x="0" y="735" width="1536" height="40"/>
      <rect class="wave-band" x="0" y="1185" width="1536" height="40"/>
      <rect class="wave-band" x="420" y="775" width="42" height="410"/>
      <rect class="wave-band" x="1078" y="775" width="42" height="410"/>

      <rect x="0" y="668" width="1536" height="30" fill="url(#gold-band)"/>
      <line class="band-rule" x1="0" y1="703" x2="1536" y2="703"/>
      <rect x="0" y="1262" width="1536" height="30" fill="url(#gold-band)"/>
      <line class="band-rule" x1="0" y1="1257" x2="1536" y2="1257"/>

      <rect x="353" y="775" width="30" height="410" fill="url(#gold-bar)"/>
      <line class="band-rule" x1="388" y1="775" x2="388" y2="1185"/>
      <rect x="1153" y="775" width="30" height="410" fill="url(#gold-bar)"/>
      <line class="band-rule" x1="1148" y1="775" x2="1148" y2="1185"/>
    </g>

    <!-- floral bouquets -->
    <ellipse cx="575" cy="610" rx="98" ry="125" fill="url(#bouquet-tone)" role="img" aria-label="Bouquet of roses and white wild flowers with leaves"/>
    <ellipse cx="965" cy="1350" rx="98" ry="125" fill="url(#bouquet-tone)" role="img" aria-label="Bouquet of roses and white wild flowers with leaves"/>

    <!-- taglines -->
    <text class="tagline tagline--gold" x="920" y="650" text-anchor="middle">Spread the frangrance</text>
    <text class="tagline tagline--navy" x="920" y="691" text-anchor="middle">of Charity</text>
    <g transform="rotate(180 618 1295)">
      <text class="tagline tagline--gold" x="618" y="1278" text-anchor="middle">Spread the frangrance</text>
      <text class="tagline tagline--navy" x="618" y="1319" text-anchor="middle">of Charity</text>
    </g>

    <!-- brand placements -->
    <g class="brand-mark">
      <text class="brand-name" x="866" y="417">Kindred Hearth</text>
      <circle cx="1045" cy="411" r="10" fill="var(--gold-mid)"/>
      <text class="brand-note" x="866" y="433">Sample Logo Placement</text>
    </g>
    <g class="brand-mark" transform="rotate(180 766 295)">
      <text class="brand-name" x="656" y="301">Kindred Hearth</text>
      <circle cx="835" cy="295" r="10" fill="var(--gold-mid)"/>
      <text class="brand-note" x="656" y="317">Sample Logo Placement</text>
    </g>

    <!-- cutting lines -->
    <path class="cut-line" d="M462 365 L690 176 V150 A20 20 0 0 1 710 130 H828 A20 20 0 0 1 848 150 V176 L1078 365 L1430 980 L1078 1595 H894 V1660 Q894 1695 860 1708 Q894 1722 894 1760 V1868 H644 V1760 Q644 1722 678 1708 Q644 1695 644 1660 V1595 H462 L107 980 Z"/>
    <rect class="cut-line" x="693" y="474" width="152" height="22" rx="11"/>
    <rect class="cut-line" x="690" y="1397" width="158" height="10" rx="5"/>
    <path class="cut-line" d="M690 1595 V1640 A25 25 0 0 0 715 1665 H823 A25 25 0 0 0 848 1640 V1595"/>
    <path class="cut-line" d="M690 1822 V1780 A25 25 0 0 1 715 1755 H823 A25 25 0 0 1 848 1780 V1822 Z"/>

    <!-- folding lines -->
    <rect class="fold-line" x="462" y="365" width="616" height="1230"/>
    <line class="fold-line" x1="462" y1="775" x2="1078" y2="775"/>
    <line class="fold-line" x1="462" y1="1185" x2="1078" y2="1185"/>
    <line class="fold-line" x1="690" y1="176" x2="848" y2="176"/>
    <line class="fold-line" x1="644" y1="1708" x2="894" y2="1708"/>
    <path class="fold-line" d="M462 775 L107 980 L462 1185 M285 672 L462 775 M462 1185 L285 1290"/>
    <path class="fold-line" d="M1078 775 L1430 980 L1078 1185 M1255 672 L1078 775 M1078 1185 L1255 1290"/>

    <!-- legend -->
    <line class="cut-line" x1="1096" y1="1788" x2="1254" y2="1788"/>
    <text class="legend-label" x="1279" y="1798">Cutting Line</text>
    <line class="fold-line" x1="1096" y1="1844" x2="1254" y2="1844"/>
    <text class="legend-label" x="1279" y="1854">Folding Line</text>
  </svg>
</main>
</body>
</html>
```